Mobile Accessory Business - Brightfern - Needs Retail Packaging!

**ECO Design is not working we need to change it**

We need retail packaging designed for mobile phone accessories. This includes; mobile phone screen protectors, mobile phone cases and mobile phone cables.

We want the packaging to be simplistic, vibrant modern and minimalist.

Example:

https://www.findora-example.com.au/imgres?imgurl=https%3A%2F%2Fcdn.pixvault-example.net%2Fattachments%2Fattachment_10482761&imgrefurl=http%3A%2F%2Fcraftpitch-example.com%2Fpackaging%2Fcontests%2Fscreen-protector-packaging-551207

The packaging for each product should create a clear brand across the products i.e if a customer comes into a shop and picks up a mobile phone case they know from looking at the box's which mobile phone screen protector or mobile phone cable is ours.

We are a new company that does not provide cheap "tradly" accessories. We provide luxury accessories at a premium price.

We need a package designed for each of the following:

1) Mobile Phone Screen Protectors - The packaging needs to be standard hang cell size (for the mobile phone industry). The dimensions of the packaging should be: 18cm (H) X 10.5cm (W) and include a hanging hook. The thickness should be similar to the thickness of an envelope. This does not need a window for viewing the product as its a simple screen protector (which is essentially a clear sheet of contact).

Features: 9H (hardness), Completely flexible, they are not actually glass (made up of a nano technology, call it Lumo Plate, Hydrophobic (keeps fingerprints off), 99% transparent, does not smash like glass.

2) Mobile Phone Cases - The packaging needs to be standard hang cell size (for the mobile phone industry). The dimensions of the packaging should be: 18cm (H) X 10.5cm (W) X 2cm (D) and include a hanging hook. The product should have a viewing window so the entire contents can be see. The product should be easily and readily removed without causing damage to the contents or the packaging.

E.g (only more vibrant) https://www.findora-example.com.au/search?q=mobile+phone+case+packaging&tbm=isch#q=phone+case+packaging&imgrc=Qx7PlmRtaVwZdK%3A

Features: Whilst we will be selling several types of cases start with a design for leather cases, 100% genuine lather (first layer cow hide), TPU insert instead of hard plastic for more protection, 3 card slots,

3) Mobile Phone Cables (USB etc) - The packaging needs to be standard hang cell size (for the mobile phone industry). The dimensions of the packaging should be: 18cm (H) X 5cm (W) X 2cm (D) and include a hanging hook. The product should have a viewing window so the entire contents can be see.

E.g. (only with a viewing window) https://www.findora-example.com.au/search?q=mobile+phone+case+packaging&tbm=isch#q=micro%20usb%20packaging&imgrc=Hb3WqnTzLe8kYp%3A

Features: Braided (for strength), reversible (doesn't matter which way you plug it in), 2m in length.

The packaging for the cases needs to be accessible so customers can open it and view the case. Finally we need a window on the packaging so the product can be viewed (cable and cases)

Target Market(s)

The target market is very broad. Everyone from teenagers to the middle age purchase mobile phone accessories.

At our core is 14 --> 45 males and females.

These accessories are primarily sold in Corvana (and alike) shops in rural area's of Australia.

Industry/Entity Type

Telecommunications

Font styles to use
Serif
Sans Serif

Colors
0292cd
6b449b
00a990
9bcb3c

Requirements
Must have
• Designs for the three products mentioned in the description.
• We want the packaging to be simplistic, vibrant modern and minimalist
• Placeholders on the front for USP's.
• ******************************************************
• What needs to be on screen protectors
• FRONT
• Logo
• Heading
• (1) Scratch Resistant
• (2) Impact Resistant
• Sub-Heading
• (1) Screen Protector
• Unique Selling Points
• Space for 5 unique selling points
• BACK
• Logo
• Product Description
• Space for 6 lines
• Replacement Warranty
• 2 Year replacement warranty image/if you break it we replace it
• Barcode
• Space big enough for barcode to be stuck on
• Email Address
• This is an example of what would be written on the back of the case packaging
• "Brightfern accessories is an Australian
• owned company providing high quality
• products. We know how important it is
• for your device to be protected, so now
• your device has its own brightfern made
• from the highest quality leather and
• hand stitched to perfection."
• Contact Details:
• Email: sales@brightfernaccessories.com.au
• Barcode:
• We need a place to put a sticker with a barcode on the back of each set of packaging barcode will be the same size for each box.
• Warranty:
• Screen Protectors - 2 Year replacement warranty, If they break the screen protector We will replace it.
• Cases: 2 Year warranty
• Cables: 2 Year warranty

```html
<!DOCTYPE html>
<html lang="en">
<head>
<meta charset="utf-8">
<title>Brightfern retail packaging – case, screen and cable hang cells</title>
<link rel="stylesheet" href="https://fonts.googleapis.com/css2?family=Open+Sans:wght@300;400;600&family=Roboto+Condensed:wght@700&display=swap">
<style>
  :root {
    --board-bg: #1b1b1b;
    --board-bg-deep: #101010;
    --title-ink: #ffffff;
    --ink: #ffffff;
    --ink-soft: rgba(255,255,255,0.85);
    --window-dark: #141818;
    --hook-dark: #1c2424;
  }
  html, body {
    margin: 0;
    padding: 0;
    width: 1200px;
    height: 1200px;
    overflow: hidden;
    background: var(--board-bg-deep);
  }
  .board {
    position: relative;
    width: 1200px;
    height: 1200px;
    overflow: hidden;
    background: linear-gradient(90deg, var(--board-bg-deep), var(--board-bg) 30%, var(--board-bg) 70%, var(--board-bg-deep));
    font-family: "Open Sans", Arial, sans-serif;
    color: var(--ink);
  }
  .category-title {
    position: absolute;
    top: 88px;
    margin: 0;
    font-family: "Roboto Condensed", "Arial Narrow", sans-serif;
    font-weight: 700;
    font-size: 50px;
    line-height: 1;
    color: var(--title-ink);
    transform: translateX(-50%);
  }
  .category-title--case { left: 240px; }
  .category-title--screen { left: 638px; }
  .category-title--cable { left: 1060px; }

  /* colour ranges */
  .range { position: absolute; left: 0; width: 1200px; height: 320px; }
  .range--teal {
    --tone: #17c4a3; --tone-deep: #0c9c83; --tone-light: #3ee3c2;
    --band: rgba(88,128,118,0.93); --band-light: rgba(120,160,150,0.6);
    --pill: rgba(120,235,210,0.55); --frame: #19c9a6;
    top: 177px;
  }
  .range--blue {
    --tone: #1a9ad7; --tone-deep: #0b74ae; --tone-light: #3cb8ec;
    --band: rgba(78,112,134,0.93); --band-light: rgba(110,150,175,0.6);
    --pill: rgba(110,200,240,0.55); --frame: #1a9fe0;
    top: 511px;
  }
  .range--purple {
    --tone: #7a47b8; --tone-deep: #592d92; --tone-light: #9566d2;
    --band: rgba(104,84,122,0.94); --band-light: rgba(150,120,175,0.6);
    --pill: rgba(165,120,225,0.6); --frame: #8a4fd6;
    top: 845px;
  }

  /* package base */
  .pack {
    position: absolute;
    top: 0;
    background:
      linear-gradient(90deg, rgba(255,255,255,0.08) 0 14%, transparent 14% 86%, rgba(255,255,255,0.08) 86%),
      radial-gradient(ellipse at 50% 30%, var(--tone-light), var(--tone) 60%, var(--tone-deep));
  }
  .pack--case { width: 192px; height: 292px; }
  .pack--case.pack--front { left: 24px; }
  .pack--case.pack--back { left: 246px; }
  .pack--screen { width: 172px; height: 292px; }
  .pack--screen.pack--front { left: 486px; }
  .pack--screen.pack--back { left: 682px; }
  .pack--cable { width: 76px; height: 310px; }
  .pack--cable.pack--front { left: 934px; }
  .pack--cable.pack--back { left: 1078px; }

  .hook {
    position: absolute;
    top: 15px;
    left: 50%;
    width: 46px;
    height: 7px;
    margin-left: -23px;
    border-radius: 4px;
    background: var(--hook-dark);
  }
  .hook::before {
    content: "";
    position: absolute;
    left: 50%;
    top: -5px;
    width: 14px;
    height: 10px;
    margin-left: -7px;
    border-radius: 7px 7px 0 0;
    background: var(--hook-dark);
  }
  .pack--cable .hook { width: 40px; margin-left: -20px; }

  .brand {
    position: absolute;
    margin: 0;
    font-weight: 400;
    font-size: 11px;
    line-height: 1;
    color: var(--ink);
    white-space: nowrap;
  }
  .brand-dot {
    display: inline-block;
    width: 5px;
    height: 5px;
    margin-left: 3px;
    border-radius: 50%;
    background: var(--ink);
    vertical-align: middle;
  }

  /* case front */
  .case-window {
    position: absolute;
    left: 42px;
    top: 66px;
    width: 104px;
    height: 176px;
    border: 3px solid var(--tone-deep);
    border-radius: 6px;
    background: var(--window-dark);
  }
  .band {
    position: absolute;
    left: 0;
    top: 131px;
    width: 100%;
    height: 80px;
    background:
      linear-gradient(160deg, transparent 40%, var(--band-light) 40% 58%, transparent 58%),
      var(--band);
    overflow: visible;
  }
  .band-side {
    position: absolute;
    top: 50%;
    font-size: 7.5px;
    letter-spacing: 0.3px;
    writing-mode: vertical-rl;
    transform: translateY(-50%) rotate(180deg);
    color: var(--ink-soft);
  }
  .band-side--left { left: 6px; }
  .band-side--right { right: 6px; }
  .band-title {
    position: absolute;
    margin: 0;
    font-weight: 300;
    font-size: 11px;
    line-height: 1;
    color: var(--ink);
  }
  .pack--case.pack--front .band-title { right: 95px; top: 14px; }
  .band-number {
    position: absolute;
    right: 95px;
    top: 28px;
    margin: 0;
    font-weight: 300;
    font-size: 11px;
    line-height: 1;
  }
  .feature-list {
    position: absolute;
    margin: 0;
    padding: 0;
    list-style: none;
    font-size: 4.5px;
    line-height: 1;
    color: var(--ink-soft);
  }
  .feature-list li { margin-bottom: 6px; }
  .feature-list--band { right: 95px; top: 44px; text-align: right; }
  .feature-list--band li::after {
    content: "";
    display: inline-block;
    width: 4px;
    height: 4px;
    margin-left: 3px;
    border-radius: 1px;
    background: var(--tone-light);
    vertical-align: middle;
  }
  .band-window {
    position: absolute;
    left: 101px;
    top: 8px;
    width: 54px;
    height: 57px;
    border: 3px solid var(--frame);
    border-radius: 8px;
    background: var(--window-dark);
  }

  /* case back */
  .back-copy {
    position: absolute;
    left: 37px;
    top: 8px;
    width: 125px;
  }
  .back-copy .brand { position: static; font-size: 8px; }
  .back-copy .band-title { position: static; margin-top: 4px; font-size: 8.5px; }
  .description {
    margin: 3px 0 0;
    font-size: 3.6px;
    line-height: 1.5;
    color: var(--ink-soft);
  }
  .email {
    margin: 0;
    padding-top: 3px;
    font-size: 4px;
    color: var(--ink-soft);
  }
  .rule { height: 0; border-top: 0.6px solid rgba(255,255,255,0.7); margin: 4px 0 0; }
  .warranty {
    position: absolute;
    margin: 0;
    font-size: 5.5px;
    color: var(--ink);
  }
  .pack--case.pack--back .warranty { left: 37px; top: 250px; }

  /* screen front */
  .heading-pill {
    position: absolute;
    left: 10px;
    top: 68px;
    width: 150px;
    height: 39px;
    border-radius: 20px;
    background: linear-gradient(90deg, var(--pill), rgba(255,255,255,0.08));
    text-align: center;
  }
  .heading-pill .pill-title {
    margin: 3px 0 0;
    font-weight: 300;
    font-size: 22px;
    line-height: 1.05;
    letter-spacing: 0.5px;
  }
  .heading-pill .pill-sub {
    margin: 0;
    font-size: 7.5px;
    letter-spacing: 0.8px;
    color: var(--ink-soft);
  }
  .product-art {
    position: absolute;
    left: 14px;
    top: 130px;
    width: 146px;
    height: 84px;
    border-radius: 12px;
    background: linear-gradient(160deg, rgba(255,255,255,0.35), #1e2424 45%, #0d1010 80%, var(--tone-deep));
    opacity: 0.9;
  }
  .facets {
    position: absolute;
    left: 0;
    bottom: 0;
    width: 100%;
    height: 70px;
  }
  .feature-list--screen { left: 14px; top: 235px; font-size: 4.8px; }
  .feature-list--screen li { margin-bottom: 3.6px; }
  .feature-list--screen li::before {
    content: "";
    display: inline-block;
    width: 4px;
    height: 4px;
    margin-right: 4px;
    border: 0.6px solid var(--ink-soft);
    vertical-align: middle;
  }

  /* screen back */
  .info-panel { position: absolute; left: 0; top: 170px; width: 100%; height: 122px; }
  .info-panel svg { position: absolute; inset: 0; width: 100%; height: 100%; }
  .info-copy { position: absolute; left: 13px; top: 12px; width: 150px; }
  .info-copy .brand { position: static; font-size: 9px; }
  .info-copy .band-title { position: static; margin-top: 4px; font-size: 9.5px; }
  .pack--screen.pack--back .warranty { left: 13px; top: 270px; font-size: 6.5px; }

  /* cable */
  .cable-window {
    position: absolute;
    left: 12px;
    top: 60px;
    width: 45px;
    height: 240px;
    border: 3px solid var(--tone-deep);
    border-bottom: none;
    border-radius: 26px 26px 0 0;
    background: var(--window-dark);
  }
  .band--cable {
    left: -26px;
    top: 224px;
    width: 128px;
    height: 58px;
  }
  .band--cable .band-side { font-size: 6.5px; }
  .band--cable .band-side--left { left: 5px; }
  .band--cable .band-side--right { right: 5px; }
  .cable-copy { position: absolute; left: 33px; top: 5px; width: 75px; }
  .cable-copy .brand { position: static; font-size: 6px; }
  .cable-copy .band-title { position: static; margin-top: 2px; font-size: 10px; }
  .feature-list--cable { position: static; margin-top: 3px; font-size: 3px; }
  .feature-list--cable li { margin-bottom: 2.5px; }
  .feature-list--cable li::before {
    content: "";
    display: inline-block;
    width: 2.5px;
    height: 2.5px;
    margin-right: 2px;
    background: var(--tone-light);
    vertical-align: middle;
  }
  .cable-copy .email, .cable-copy .warranty-small {
    position: static;
    margin: 0;
    font-size: 3.2px;
    color: var(--ink-soft);
  }
  .cable-copy .warranty-small { margin-top: 6px; }
</style>
</head>
<body>
<main class="board">

  <h2 class="category-title category-title--case">Case</h2>
  <h2 class="category-title category-title--screen">Screen</h2>
  <h2 class="category-title category-title--cable">Cable</h2>

  <!-- TEAL RANGE -->
  <section class="range range--teal">
    <article class="pack pack--case pack--front">
      <span class="hook"></span>
      <p class="brand" style="left:74px;top:44px">brightfern<span class="brand-dot"></span></p>
      <div class="case-window"></div>
      <div class="band">
        <span class="band-side band-side--left">HEADING</span>
        <span class="band-side band-side--right">HEADING</span>
        <h3 class="band-title">HEADING</h3>
        <p class="band-number">1</p>
        <ul class="feature-list feature-list--band"><li>feature 1</li><li>feature 2</li><li>feature 3</li></ul>
        <div class="band-window"></div>
      </div>
    </article>
    <article class="pack pack--case pack--back">
      <span class="hook"></span>
      <div class="band">
        <span class="band-side band-side--left">HEADING</span>
        <span class="band-side band-side--right">HEADING</span>
        <div class="back-copy">
          <p class="brand">brightfern<span class="brand-dot"></span></p>
          <h3 class="band-title">HEADING</h3>
          <p class="description">Description Description Description Description Description Description Description Description Description Description Description Description Description Description Description Description Description Description Description Description</p>
          <p class="email">email address</p>
        </div>
      </div>
      <p class="warranty">2 YEARS WARRANTY</p>
    </article>
    <article class="pack pack--screen pack--front">
      <span class="hook"></span>
      <p class="brand" style="left:55px;top:50px;font-size:12px">brightfern<span class="brand-dot"></span></p>
      <div class="heading-pill"><p class="pill-title">HEADING</p><p class="pill-sub">Sub Heading</p></div>
      <div class="product-art" role="img" aria-label="Phone with a screen protector peeling from its display"></div>
      <svg class="facets" viewBox="0 0 172 70" preserveAspectRatio="none" aria-hidden="true">
        <polygon points="0,30 172,0 172,70 0,70" fill="var(--tone-deep)" opacity="0.45"/>
        <polygon points="0,45 120,70 0,70" fill="var(--tone-deep)" opacity="0.6"/>
      </svg>
      <ul class="feature-list feature-list--screen"><li>features 1</li><li>features 2</li><li>features 3</li><li>features 4</li><li>features 5</li><li>features 6</li></ul>
    </article>
    <article class="pack pack--screen pack--back">
      <span class="hook"></span>
      <div class="info-panel">
        <svg viewBox="0 0 172 122" preserveAspectRatio="none" aria-hidden="true">
          <polygon points="0,0 172,0 172,122 0,122" fill="var(--tone-light)" opacity="0.35"/>
          <polygon points="60,0 172,0 172,30" fill="var(--tone-deep)" opacity="0.5"/>
          <polygon points="0,90 172,60 172,122 0,122" fill="var(--tone-deep)" opacity="0.3"/>
        </svg>
        <div class="info-copy">
          <p class="brand">brightfern<span class="brand-dot"></span></p>
          <h3 class="band-title">HEADING</h3>
          <p class="description">Description Description Description Description Description Description Description Description Description Description Description Description Description Description Description Description Description Description Description Description</p>
          <div class="rule"></div>
          <p class="email">email address</p>
          <div class="rule"></div>
        </div>
      </div>
      <p class="warranty">2 YEARS WARRANTY</p>
    </article>
    <article class="pack pack--cable pack--front">
      <span class="hook"></span>
      <div class="cable-window"></div>
      <div class="band band--cable">
        <span class="band-side band-side--left">HEADING</span>
        <span class="band-side band-side--right">HEADING</span>
        <div class="cable-copy">
          <p class="brand">brightfern<span class="brand-dot"></span></p>
          <h3 class="band-title">HEADING 1</h3>
          <ul class="feature-list feature-list--cable"><li>Feature 1</li><li>Feature 2</li><li>Feature 3</li></ul>
        </div>
      </div>
    </article>
    <article class="pack pack--cable pack--back">
      <span class="hook"></span>
      <div class="band band--cable">
        <span class="band-side band-side--left">HEADING</span>
        <span class="band-side band-side--right">HEADING</span>
        <div class="cable-copy">
          <p class="brand">brightfern<span class="brand-dot"></span></p>
          <h3 class="band-title">HEADING</h3>
          <p class="email">email address</p>
          <p class="warranty-small">2 YEARS WARRANTY</p>
        </div>
      </div>
    </article>
  </section>

  <!-- BLUE RANGE -->
  <section class="range range--blue">
    <article class="pack pack--case pack--front">
      <span class="hook"></span>
      <p class="brand" style="left:74px;top:44px">brightfern<span class="brand-dot"></span></p>
      <div class="case-window"></div>
      <div class="band">
        <span class="band-side band-side--left">HEADING</span>
        <span class="band-side band-side--right">HEADING</span>
        <h3 class="band-title">HEADING</h3>
        <p class="band-number">1</p>
        <ul class="feature-list feature-list--band"><li>feature 1</li><li>feature 2</li><li>feature 3</li></ul>
        <div class="band-window"></div>
      </div>
    </article>
    <article class="pack pack--case pack--back">
      <span class="hook"></span>
      <div class="band">
        <span class="band-side band-side--left">HEADING</span>
        <span class="band-side band-side--right">HEADING</span>
        <div class="back-copy">
          <p class="brand">brightfern<span class="brand-dot"></span></p>
          <h3 class="band-title">HEADING</h3>
          <p class="description">Description Description Description Description Description Description Description Description Description Description Description Description Description Description Description Description Description Description Description Description</p>
          <p class="email">email address</p>
        </div>
      </div>
      <p class="warranty">2 YEARS WARRANTY</p>
    </article>
    <article class="pack pack--screen pack--front">
      <span class="hook"></span>
      <p class="brand" style="left:55px;top:50px;font-size:12px">brightfern<span class="brand-dot"></span></p>
      <div class="heading-pill"><p class="pill-title">HEADING</p><p class="pill-sub">Sub Heading</p></div>
      <div class="product-art" role="img" aria-label="Phone with a screen protector peeling from its display"></div>
      <svg class="facets" viewBox="0 0 172 70" preserveAspectRatio="none" aria-hidden="true">
        <polygon points="0,30 172,0 172,70 0,70" fill="var(--tone-deep)" opacity="0.45"/>
        <polygon points="0,45 120,70 0,70" fill="var(--tone-deep)" opacity="0.6"/>
      </svg>
      <ul class="feature-list feature-list--screen"><li>Feature 1</li><li>Feature 2</li><li>Feature 3</li><li>Feature 4</li><li>Feature 5</li><li>Feature 6</li></ul>
    </article>
    <article class="pack pack--screen pack--back">
      <span class="hook"></span>
      <div class="info-panel">
        <svg viewBox="0 0 172 122" preserveAspectRatio="none" aria-hidden="true">
          <polygon points="0,0 172,0 172,122 0,122" fill="var(--tone-light)" opacity="0.35"/>
          <polygon points="60,0 172,0 172,30" fill="var(--tone-deep)" opacity="0.5"/>
          <polygon points="0,90 172,60 172,122 0,122" fill="var(--tone-deep)" opacity="0.3"/>
        </svg>
        <div class="info-copy">
          <p class="brand">brightfern<span class="brand-dot"></span></p>
          <h3 class="band-title">HEADING</h3>
          <p class="description">Description Description Description Description Description Description Description Description Description Description Description Description Description Description Description Description Description Description Description Description</p>
          <div class="rule"></div>
          <p class="email">email address</p>
          <div class="rule"></div>
        </div>
      </div>
      <p class="warranty">2 YEARS WARRANTY</p>
    </article>
    <article class="pack pack--cable pack--front">
      <span class="hook"></span>
      <div class="cable-window"></div>
      <div class="band band--cable">
        <span class="band-side band-side--left">HEADING</span>
        <span class="band-side band-side--right">HEADING</span>
        <div class="cable-copy">
          <p class="brand">brightfern<span class="brand-dot"></span></p>
          <h3 class="band-title">HEADING 1</h3>
          <ul class="feature-list feature-list--cable"><li>Feature 1</li><li>Feature 2</li><li>Feature 3</li></ul>
        </div>
      </div>
    </article>
    <article class="pack pack--cable pack--back">
      <span class="hook"></span>
      <div class="band band--cable">
        <span class="band-side band-side--left">HEADING</span>
        <span class="band-side band-side--right">HEADING</span>
        <div class="cable-copy">
          <p class="brand">brightfern<span class="brand-dot"></span></p>
          <h3 class="band-title">HEADING</h3>
          <p class="email">email address</p>
          <p class="warranty-small">2 YEARS WARRANTY</p>
        </div>
      </div>
    </article>
  </section>

  <!-- PURPLE RANGE -->
  <section class="range range--purple">
    <article class="pack pack--case pack--front">
      <span class="hook"></span>
      <p class="brand" style="left:74px;top:44px">brightfern<span class="brand-dot"></span></p>
      <div class="case-window"></div>
      <div class="band">
        <span class="band-side band-side--left">HEADING</span>
        <span class="band-side band-side--right">HEADING</span>
        <h3 class="band-title">HEADING</h3>
        <p class="band-number">1</p>
        <ul class="feature-list feature-list--band"><li>feature 1</li><li>feature 2</li><li>feature 3</li></ul>
        <div class="band-window"></div>
      </div>
    </article>
    <article class="pack pack--case pack--back">
      <span class="hook"></span>
      <div class="band">
        <span class="band-side band-side--left">HEADING</span>
        <span class="band-side band-side--right">HEADING</span>
        <div class="back-copy">
          <p class="brand">brightfern<span class="brand-dot"></span></p>
          <h3 class="band-title">HEADING</h3>
          <p class="description">Description Description Description Description Description Description Description Description Description Description Description Description Description Description Description Description Description Description Description Description</p>
          <p class="email">email address</p>
        </div>
      </div>
      <p class="warranty">2 YEARS WARRANTY</p>
    </article>
    <article class="pack pack--screen pack--front">
      <span class="hook"></span>
      <p class="brand" style="left:55px;top:50px;font-size:12px">brightfern<span class="brand-dot"></span></p>
      <div class="heading-pill"><p class="pill-title">HEADING</p><p class="pill-sub">Sub Heading</p></div>
      <div class="product-art" role="img" aria-label="Phone with a screen protector peeling from its display"></div>
      <svg class="facets" viewBox="0 0 172 70" preserveAspectRatio="none" aria-hidden="true">
        <polygon points="0,30 172,0 172,70 0,70" fill="var(--tone-deep)" opacity="0.45"/>
        <polygon points="0,45 120,70 0,70" fill="var(--tone-deep)" opacity="0.6"/>
      </svg>
      <ul class="feature-list feature-list--screen"><li>Feature 1</li><li>Feature 2</li><li>Feature 3</li><li>Feature 4</li><li>Feature 5</li><li>Feature 6</li></ul>
    </article>
    <article class="pack pack--screen pack--back">
      <span class="hook"></span>
      <div class="info-panel">
        <svg viewBox="0 0 172 122" preserveAspectRatio="none" aria-hidden="true">
          <polygon points="0,0 172,0 172,122 0,122" fill="var(--tone-light)" opacity="0.35"/>
          <polygon points="60,0 172,0 172,30" fill="var(--tone-deep)" opacity="0.5"/>
          <polygon points="0,90 172,60 172,122 0,122" fill="var(--tone-deep)" opacity="0.3"/>
        </svg>
        <div class="info-copy">
          <p class="brand">brightfern<span class="brand-dot"></span></p>
          <h3 class="band-title">HEADING</h3>
          <p class="description">Description Description Description Description Description Description Description Description Description Description Description Description Description Description Description Description Description Description Description Description</p>
          <div class="rule"></div>
          <p class="email">email address</p>
          <div class="rule"></div>
        </div>
      </div>
      <p class="warranty">2 YEARS WARRANTY</p>
    </article>
    <article class="pack pack--cable pack--front">
      <span class="hook"></span>
      <div class="cable-window"></div>
      <div class="band band--cable">
        <span class="band-side band-side--left">HEADING</span>
        <span class="band-side band-side--right">HEADING</span>
        <div class="cable-copy">
          <p class="brand">brightfern<span class="brand-dot"></span></p>
          <h3 class="band-title">HEADING 1</h3>
          <ul class="feature-list feature-list--cable"><li>Feature 1</li><li>Feature 2</li><li>Feature 3</li></ul>
        </div>
      </div>
    </article>
    <article class="pack pack--cable pack--back">
      <span class="hook"></span>
      <div class="band band--cable">
        <span class="band-side band-side--left">HEADING</span>
        <span class="band-side band-side--right">HEADING</span>
        <div class="cable-copy">
          <p class="brand">brightfern<span class="brand-dot"></span></p>
          <h3 class="band-title">HEADING</h3>
          <p class="email">email address</p>
          <p class="warranty-small">2 YEARS WARRANTY</p>
        </div>
      </div>
    </article>
  </section>

</main>
</body>
</html>
```